Futuristic and Visually Appealing Photo Booth Rental Website

I need a Photo Booth rental website made for easy editing through Wordpress. Web design + Page Templates are needed for showcasing booths, packages, experiences, and add-ons. There's a space and futuristic theme to the company that I'd like to stick with. I'd like to integrate certain parts of the site with html code (iframe) but others with text, pictures, and video. I'd like the design as complete as possible while I help work on the content as much as I can. The priority should be making the site friendly enough to educate and convert sales/bookings. I have no problem working from a general photobooth website as a base.

Company: SnapTrek NX

Coding required. All source files needed to install as theme that can be edited by something like Elementor.

**Contact for current design done under maintenance mode**

Target Market(s)

All consumers (holiday parties, birthdays, weddings, etc...)
Corporate Clients (conventions, virtual expos, holiday parties, company events)

Industry/Entity Type

Events

Coding

Coded - Design and coding required

Font styles to use
Sans Serif

Requirements
Must have
• ===Menu/Submenu===
Our Booths: DSLR Open Air Photo Booth, Selfie Station, Drifta, Pendulum Skiv, LumaVex
Consumers: Rental Packages, Addons
Corporate: Experiences, Addons, Build-to-Suit, Get a Quote (iframe)
About: About Us, Non-Profits, Employment
Customizations: Printout Templates (iframe), Start Screens (iframe), Backdrops
Contact Us: Inquiry, Custom Quote

===Buttons/Call to Action===
Book Online
Find My Photos
Client Portal

Social Media Icons and Footer section for vendor buttons (vowlinker, quib, the plume, etc...)

Responsive design
Nice to have
• Video Slides on Frontpage
Should not have
• OnePage Design

```html
<!DOCTYPE html>
<html lang="en">
<head>
<meta charset="utf-8">
<title>SnapTrek NX — Photo Booth Rental</title>
<link href="https://fonts.googleapis.com/css2?family=Titillium+Web:wght@300;400;600;700&display=swap" rel="stylesheet">
<style>
:root{
  --space:#0b0f24;
  --space-deep:#070a19;
  --teal:#1ec8c8;
  --teal-bright:#35e0dc;
  --card:#141a46;
  --card-head:#1c2366;
  --violet:#7b3fd6;
  --magenta:#d23ca8;
  --white:#ffffff;
  --muted:#a9b0d6;
  --footer:#0a0d1e;
}
*{margin:0;padding:0;box-sizing:border-box}
html,body{width:1200px;height:3556px;overflow:hidden}
body{
  font-family:"Titillium Web",Arial,sans-serif;color:var(--white);
  background:
    radial-gradient(ellipse 700px 500px at 30% 1500px,rgba(60,70,160,.25),transparent),
    radial-gradient(ellipse 600px 400px at 80% 2000px,rgba(90,60,170,.2),transparent),
    var(--space);
  position:relative;
}
a{color:inherit;text-decoration:none}

/* header */
.topbar{position:absolute;top:30px;left:140px;right:140px;display:flex;justify-content:space-between;font-size:15px;z-index:3}
.topbar span{display:inline-flex;align-items:center;gap:8px;margin-right:26px}
.topbar .right span{margin:0 0 0 26px}
.dot{width:10px;height:10px;border-radius:50%;background:var(--magenta)}
.nav{position:absolute;top:86px;left:140px;right:140px;display:flex;justify-content:space-between;align-items:center;font-size:17px;font-weight:600;z-index:3}
.nav .group{display:flex;gap:30px;align-items:center}
.nav .active{background:var(--teal);padding:4px 16px;border-radius:18px}
.brand{position:absolute;left:530px;top:6px;width:140px;height:140px;border-radius:50%;background:var(--space-deep);border:3px solid var(--teal);display:flex;align-items:center;justify-content:center;font-weight:700;font-size:19px;z-index:4}

/* hero */
.hero{position:absolute;top:0;left:0;width:1200px;height:960px;overflow:hidden;
  background:linear-gradient(#0a0c22,#141038 60%,#0b0f24)}
.hero-visual{position:absolute;left:0;top:0;width:1200px;height:900px;
  background:linear-gradient(135deg,rgba(30,30,90,.2) 0%,rgba(110,60,200,.45) 45%,rgba(190,60,170,.4) 75%,rgba(20,20,60,.2) 100%)}
.hero-title{position:absolute;left:140px;top:360px;font-size:58px;line-height:1.05;font-weight:700;letter-spacing:1px}
.btn{display:inline-block;font-size:12px;font-weight:700;text-transform:uppercase;padding:8px 18px;border-radius:3px}
.btn-outline{border:2px solid var(--white)}
.btn-teal{background:var(--teal)}
.hero .btn-outline{position:absolute;left:140px;top:565px}
.hero .btn-teal{position:absolute;left:140px;top:616px;padding:8px 30px}
.arrow{position:absolute;width:40px;height:40px;border-radius:50%;background:var(--white);display:flex;align-items:center;justify-content:center}
.hero-arc{position:absolute;left:0;top:780px}

/* booths */
.section-title{font-size:44px;font-weight:700;color:var(--teal);letter-spacing:1px}
.booths{position:absolute;top:1000px;left:140px;width:920px}
.booth-list{margin-top:26px;width:480px;list-style:none}
.booth-list li{height:62px;border:2px solid var(--white);margin-bottom:14px;display:flex;align-items:center;font-size:23px;font-weight:600;position:relative;padding-left:66px}
.booth-list li::before{content:"";position:absolute;left:0;top:0;bottom:0;width:44px;border-right:2px solid var(--white)}
.booth-list li svg{position:absolute;left:14px}
.booth-list .open{background:var(--teal);border-color:var(--teal-bright);color:var(--space-deep);padding-left:20px}
.booth-list .open::before{left:auto;right:0;border-right:none;border-left:2px solid var(--space-deep)}
.booth-list .open svg{left:auto;right:14px}
.booth-visual{position:absolute;left:680px;top:0;width:260px;height:560px;border-radius:6px;
  background:linear-gradient(180deg,rgba(220,224,238,.55),rgba(120,128,170,.35) 60%,rgba(40,46,100,.3))}

/* pricing */
.pricing{position:absolute;top:1580px;left:140px;width:920px;display:flex;gap:10px}
.plan{flex:1;background:var(--card);height:560px;text-align:center}
.plan-head{background:var(--card-head);padding:34px 0 24px;clip-path:polygon(0 0,100% 0,100% 86%,50% 100%,0 86%)}
.plan-head small{display:block;font-size:22px;font-weight:400}
.plan-head strong{display:block;font-size:40px;line-height:1.1}
.plan-head em{font-style:normal;font-size:14px}
.plan ul{list-style:none;margin-top:36px;font-size:15px;line-height:33px}
.plan li.faded{color:#5a63b8}
.plan .btn-teal{margin-top:30px;font-size:14px;padding:10px 22px}

/* experiences */
.experiences{position:absolute;top:2290px;left:0;width:1200px;height:690px;
  background:radial-gradient(ellipse 500px 260px at 600px 350px,rgba(200,130,60,.18),transparent),
  radial-gradient(ellipse 700px 300px at 600px 340px,rgba(90,80,200,.28),transparent),var(--space-deep)}
.experiences h2{position:absolute;top:110px;width:100%;text-align:center;font-size:36px;letter-spacing:1px}
.experiences .lead{position:absolute;top:166px;left:290px;width:620px;text-align:center;font-size:13px;color:var(--muted);line-height:1.4}
.client-photo{position:absolute;left:225px;top:290px;width:170px;height:170px;border-radius:50%;border:4px solid var(--white);background:linear-gradient(135deg,#6b5a7a,#c89a8a,#3a3050)}
.quote{position:absolute;left:470px;top:290px;width:440px;font-size:15px;line-height:1.45}
.quote-mark{position:absolute;font-size:90px;font-weight:700;line-height:1}
.quote cite{display:block;font-style:normal;margin-top:8px;color:var(--muted)}
.stars{letter-spacing:2px;font-size:13px}
.exp-arc{position:absolute;left:0;top:0}

/* footer */
.footer{position:absolute;top:3040px;left:140px;width:920px;display:flex}
.footer h3{font-size:20px;font-weight:700;letter-spacing:1px;margin-bottom:26px}
.signup{width:370px}
.signup .field{height:42px;background:var(--white);color:#888;font-size:13px;display:flex;align-items:center;padding-left:12px}
.signup .btn-teal{display:block;text-align:center;margin-top:8px;font-size:14px;padding:10px}
.vendors{display:flex;gap:30px;margin-top:30px;font-size:24px;font-weight:600;color:#8a90b0;align-items:center}
.contact{margin-left:110px;width:260px;font-size:14px;line-height:1.4}
.contact .row{display:flex;gap:14px;margin-bottom:20px}
.contact svg{flex:none;margin-top:3px}
.links{margin-left:auto;width:150px}
.links ul{list-style:none;font-size:14px;line-height:23px}
.bottombar{position:absolute;top:3440px;left:0;width:1200px;height:116px;background:var(--footer);border-top:1px solid #1d2140}
.bottombar p{position:absolute;left:140px;top:40px;font-size:14px;color:var(--muted)}
.socials{position:absolute;right:140px;top:34px;display:flex;gap:10px}
.socials span{width:30px;height:30px;border-radius:50%;border:2px solid var(--white)}
</style>
</head>
<body>

<section class="hero">
  <div class="hero-visual" role="img" aria-label="Hero photo: a photo booth kiosk in front of a neon light installation"></div>
  <h1 class="hero-title">PHOTO<br>BOOTH<br>RENTAL</h1>
  <a class="btn btn-outline">Find my photos</a>
  <a class="btn btn-teal">Book online</a>
  <div class="arrow" style="left:16px;top:480px"><svg width="14" height="14" viewBox="0 0 14 14"><path d="M9 2 4 7l5 5" stroke="#0b0f24" stroke-width="2.4" fill="none"/></svg></div>
  <div class="arrow" style="right:16px;top:480px"><svg width="14" height="14" viewBox="0 0 14 14"><path d="M5 2l5 5-5 5" stroke="#0b0f24" stroke-width="2.4" fill="none"/></svg></div>
  <svg class="hero-arc" width="1200" height="180" viewBox="0 0 1200 180">
    <path d="M0 40 Q600 250 1200 40 V180 H0Z" fill="#0b0f24"/>
    <path d="M0 40 Q600 250 1200 40" stroke="#1ec8c8" stroke-width="10" fill="none"/>
    <path d="M0 60 Q600 230 1200 60" stroke="#1ec8c8" stroke-opacity=".35" stroke-width="4" fill="none"/>
  </svg>
</section>

<div class="topbar">
  <div class="left"><span><i class="dot"></i>Client Login</span><span><i class="dot"></i>Find My Photos</span></div>
  <div class="right"><span><i class="dot"></i>702-555-0147</span><span><i class="dot"></i>hello@snaptreknx.com</span></div>
</div>
<nav class="nav">
  <div class="group"><a class="active">Our Booths</a><a>Consumers</a><a>Corporate</a></div>
  <div class="group"><a>About</a><a>Customizations</a><a>Contact Us</a></div>
</nav>
<div class="brand">SnapTrek NX</div>

<section class="booths">
  <h2 class="section-title">OUR BOOTHS</h2>
  <ul class="booth-list">
    <li class="open">DSLR Open Air Photo Booth<svg width="14" height="14" viewBox="0 0 14 14"><path d="M5 2l5 5-5 5" stroke="#070a19" stroke-width="2.4" fill="none"/></svg></li>
    <li><svg width="14" height="14" viewBox="0 0 14 14"><path d="M5 2l5 5-5 5" stroke="#fff" stroke-width="2.4" fill="none"/></svg>Selfie Station</li>
    <li><svg width="14" height="14" viewBox="0 0 14 14"><path d="M5 2l5 5-5 5" stroke="#fff" stroke-width="2.4" fill="none"/></svg>Drifta</li>
    <li><svg width="14" height="14" viewBox="0 0 14 14"><path d="M5 2l5 5-5 5" stroke="#fff" stroke-width="2.4" fill="none"/></svg>Pendulum Skiv</li>
    <li><svg width="14" height="14" viewBox="0 0 14 14"><path d="M5 2l5 5-5 5" stroke="#fff" stroke-width="2.4" fill="none"/></svg>LumaVex</li>
  </ul>
  <div class="booth-visual" role="img" aria-label="Product photo of the DSLR open air photo booth"></div>
</section>

<section class="pricing">
  <div class="plan">
    <div class="plan-head"><small>STARTING AT</small><strong>$000</strong><em>includes 3 hours</em></div>
    <ul><li>Nulla facilisi</li><li>Etiam vel massa</li><li>Cras sollicitudin cursus</li><li class="faded">Aliquam erat</li><li class="faded">Vivamus lacus justo</li><li class="faded">Pellentesque convallis</li></ul>
    <a class="btn btn-teal">Book online</a>
  </div>
  <div class="plan">
    <div class="plan-head"><small>STARTING AT</small><strong>$000</strong><em>includes 3 hours</em></div>
    <ul><li>Nulla facilisi</li><li>Etiam vel massa</li><li>Cras sollicitudin cursus</li><li class="faded">Aliquam erat</li><li class="faded">Vivamus lacus justo</li><li class="faded">Pellentesque convallis</li></ul>
    <a class="btn btn-teal">Book online</a>
  </div>
  <div class="plan">
    <div class="plan-head"><small>STARTING AT</small><strong>$000</strong><em>includes 3 hours</em></div>
    <ul><li>Nulla facilisi</li><li>Etiam vel massa</li><li>Cras sollicitudin cursus</li><li class="faded">Aliquam erat</li><li class="faded">Vivamus lacus justo</li><li class="faded">Pellentesque convallis</li></ul>
    <a class="btn btn-teal">Book online</a>
  </div>
</section>

<section class="experiences">
  <svg class="exp-arc" width="1200" height="690" viewBox="0 0 1200 690">
    <path d="M0 0 H1200 V90 Q600 -30 0 90Z" fill="#0b0f24"/>
    <path d="M0 90 Q600 -30 1200 90" stroke="#1ec8c8" stroke-width="10" fill="none"/>
    <path d="M0 600 Q600 720 1200 600 V690 H0Z" fill="#0b0f24"/>
    <path d="M0 600 Q600 720 1200 600" stroke="#1ec8c8" stroke-width="10" fill="none"/>
  </svg>
  <h2>EXPERIENCES</h2>
  <p class="lead">Guests step into our booths and leave with prints, clips and stories worth sharing. Here is what hosts say after the lights go down.</p>
  <div class="arrow" style="left:150px;top:355px;background:none"><svg width="18" height="22" viewBox="0 0 18 22"><path d="M13 2 4 11l9 9" stroke="#fff" stroke-width="3" fill="none"/></svg></div>
  <div class="arrow" style="right:150px;top:355px;background:none"><svg width="18" height="22" viewBox="0 0 18 22"><path d="M5 2l9 9-9 9" stroke="#fff" stroke-width="3" fill="none"/></svg></div>
  <div class="client-photo" role="img" aria-label="Portrait photo of a happy client at an event"></div>
  <span class="quote-mark" style="left:410px;top:270px">&ldquo;</span>
  <div class="quote">Sed ut perspiciatis unde omnis iste natus error sit voluptatem accusantium doloremque laudantium, totam rem aperiam, eaque ipsa quae ab illo inventore veritatis et quasi architecto beatae vitae dicta sunt explicabo. Nemo enim ipsam voluptatem quia voluptas.<cite>Marcus Fenwell<br><span class="stars">★★★★★</span></cite></div>
  <span class="quote-mark" style="left:870px;top:420px">&rdquo;</span>
</section>

<footer class="footer">
  <div class="signup">
    <h3>EMAIL SIGN UP</h3>
    <div class="field">Enter Email Address</div>
    <a class="btn btn-teal">Subscribe</a>
    <div class="vendors"><span>vowlinker</span><span>quib</span><span>the plume</span></div>
  </div>
  <div class="contact">
    <h3>CONTACT US</h3>
    <div class="row"><svg width="14" height="18" viewBox="0 0 14 18"><path d="M7 1a6 6 0 0 1 6 6c0 4-6 10-6 10S1 11 1 7a6 6 0 0 1 6-6Z" fill="#1ec8c8"/><circle cx="7" cy="7" r="2.2" fill="#0b0f24"/></svg><div>SnapTrek NX<br>4120 Orbit Ave, Suite 210<br>Las Vegas, NV 89101</div></div>
    <div class="row"><svg width="16" height="16" viewBox="0 0 16 16"><path d="M3 1h3l1.5 4-2 1.5a9 9 0 0 0 4 4L11 8.5l4 1.5v3a2 2 0 0 1-2 2A13 13 0 0 1 1 3a2 2 0 0 1 2-2Z" fill="#1ec8c8"/></svg><div>Phone :<br>702-555-0147</div></div>
    <div class="row"><svg width="16" height="12" viewBox="0 0 16 12"><rect width="16" height="12" rx="1.5" fill="#1ec8c8"/><path d="M1 1l7 6 7-6" stroke="#0b0f24" stroke-width="1.5" fill="none"/></svg><div>E - Mail :<br>hello@snaptreknx.com</div></div>
  </div>
  <div class="links">
    <h3>QUICK LINKS</h3>
    <ul><li>Home</li><li>Our Booths</li><li>Consumers</li><li>Corporate</li><li>About</li><li>Customizations</li><li>Contact Us</li></ul>
  </div>
</footer>

<div class="bottombar">
  <p>© Copyright 2020 SnapTrek NX. All Rights Reserved.</p>
  <div class="socials"><span></span><span></span><span></span></div>
</div>

</body>
</html>
```